Business Card Design for Occupational Medicine Start Up Company

We need to design a professional business card. We are a healthcare company providing occupational medicine services to blue collar industries. We are professional, efficient and high quality service providers.

Target Market(s)

Blue Collar Industry: Shipbuilding, Ports, Trucking Companies; The Executives and Safety Officers for these companies

Industry/Entity Type

Healthcare

Contact Information for Business Card

Logo, Name, Title, Email, Phone

Other font styles liked:
• Please match our Brand Guide

Requirements
Must have
• Our Company Colors and Logo

```html
<!DOCTYPE html>
<html lang="en">
<head>
<meta charset="utf-8">
<title>CrewWell Clinics — Business Card</title>
<link rel="stylesheet" href="https://fonts.googleapis.com/css2?family=Montserrat:wght@700&family=Open+Sans:wght@400;600&display=swap">
<style>
  :root {
    --navy: #2e3283;
    --sky: #27a8e0;
    --amber: #f5b24f;
    --paper: #ffffff;
    --ink-soft: #4a4a55;
    --stage: #e6e7eb;
  }
  * { box-sizing: border-box; margin: 0; padding: 0; }
  html, body { width: 1200px; height: 913px; overflow: hidden; }
  body {
    background: var(--stage);
    display: flex;
    flex-direction: column;
    align-items: center;
    justify-content: center;
    gap: 56px;
  }
  .card {
    width: 620px;
    height: 354px;
    border-radius: 22px;
    position: relative;
    overflow: hidden;
    box-shadow: 0 10px 28px rgba(0,0,0,0.18);
  }
  .wordmark {
    font-family: "Montserrat", sans-serif;
    font-weight: 700;
    letter-spacing: 0.02em;
    line-height: 1;
    white-space: nowrap;
    display: flex;
    align-items: center;
    gap: 12px;
  }
  .wordmark .dot {
    width: 18px; height: 18px; border-radius: 50%; flex: none;
  }

  /* Front */
  .card-front { background: var(--navy); }
  .card-front .wordmark {
    position: absolute;
    right: 48px;
    top: 50%;
    transform: translateY(-50%);
    color: var(--paper);
    font-size: 34px;
  }
  .card-front .dot { background: var(--amber); }

  /* Back */
  .card-back { background: var(--paper); }
  .card-back .wordmark {
    position: absolute;
    left: 40px;
    top: 157px;
    width: 256px;
    color: var(--navy);
    font-size: 20px;
    gap: 10px;
  }
  .card-back .dot { background: var(--sky); width: 14px; height: 14px; }
  .divider {
    position: absolute;
    left: 318px; top: 92px;
    width: 1.5px; height: 150px;
    background: var(--amber);
  }
  .contact {
    position: absolute;
    left: 340px; top: 86px;
    font-family: "Open Sans", sans-serif;
    color: var(--ink-soft);
  }
  .contact .name {
    font-family: "Montserrat", sans-serif;
    font-weight: 700;
    color: var(--navy);
    font-size: 21px;
    letter-spacing: 0.01em;
  }
  .contact .title { font-size: 15px; margin-top: 2px; }
  .contact ul { list-style: none; margin-top: 18px; }
  .contact li {
    display: flex; align-items: center; gap: 9px;
    font-size: 14.5px; line-height: 1.75;
  }
  .contact svg { width: 13px; height: 13px; flex: none; }
  .icon-fill { fill: var(--sky); }
  .icon-line { fill: none; stroke: var(--paper); stroke-width: 2; }
  .band {
    position: absolute; left: 0; right: 0; bottom: 0;
    height: 12px; display: flex;
  }
  .band span:nth-child(1) { flex: 56; background: var(--navy); }
  .band span:nth-child(2) { flex: 26; background: var(--sky); }
  .band span:nth-child(3) { flex: 18; background: var(--amber); }
</style>
</head>
<body>
  <section class="card card-front">
    <div class="wordmark"><span class="dot"></span>CREWWELL CLINICS</div>
  </section>

  <section class="card card-back">
    <div class="wordmark"><span class="dot"></span>CREWWELL CLINICS</div>
    <div class="divider"></div>
    <div class="contact">
      <p class="name">MARK DELANEY</p>
      <p class="title">President</p>
      <ul>
        <li>
          <svg viewBox="0 0 24 24" aria-hidden="true"><path class="icon-fill" d="M6.6 10.8a15.1 15.1 0 0 0 6.6 6.6l2.2-2.2a1 1 0 0 1 1-.25 11.4 11.4 0 0 0 3.6.57 1 1 0 0 1 1 1V21a1 1 0 0 1-1 1A18 18 0 0 1 2 4a1 1 0 0 1 1-1h3.5a1 1 0 0 1 1 1c0 1.25.2 2.45.57 3.6a1 1 0 0 1-.25 1z"/></svg>
          555-310-2287
        </li>
        <li>
          <svg viewBox="0 0 24 24" aria-hidden="true"><rect class="icon-fill" x="2" y="5" width="20" height="14" rx="1.5"/><path class="icon-line" d="M3 6l9 7 9-7"/></svg>
          mark@crewwellclinics.com
        </li>
        <li>
          <svg viewBox="0 0 24 24" aria-hidden="true"><circle class="icon-fill" cx="12" cy="12" r="10"/></svg>
          www.crewwellclinics.com
        </li>
      </ul>
    </div>
    <div class="band"><span></span><span></span><span></span></div>
  </section>
</body>
</html>
```